Corporate Two Sided Business Card

Looking for a Corporate "edgy" Modern look and feel for a business card

We are looking at two options. Dark background with our logo on it, white background with our logo on it - The background is more - Charcoal / Graphite then black

Details will be

Rosalind Tebb

Licensee / Director

m. 0452 918 604

e. rosalind@quarvelhome.com.au

quarvelhome.com.au

Target Market(s)

Professional Business people that refer use business and clients that own Investment Properties

Industry/Entity Type

Business

Contact Information for Business Card

Details will be

Rosalind Tebb

Licensee / Director

m. 0452 918 604

quarvelhome.com.au

Font styles to use
Serif

Colors
000000
ec1f27
eeeeee
ffffff

Requirements
Must have
• Two options - White Background and Dark Background. - Two sided
Nice to have
• A design that is edgy, modern and new to look instead of boring style corporate cards - It should be a full integrated design
Should not have
• Block looking - Cheap.

```html
<!DOCTYPE html>
<html lang="en">
<head>
<meta charset="utf-8">
<title>Quarvel Home – Business Card</title>
<link rel="stylesheet" href="https://fonts.googleapis.com/css2?family=Poppins:wght@500&family=Roboto+Condensed:wght@700&family=Roboto:wght@400;500&display=swap">
<style>
  :root {
    --stage: #1c1c1c;
    --card-light: #f7f7f7;
    --card-dark: #2a2a2b;
    --brand-red: #ec1f27;
    --ink-grey: #4a4a4c;
    --url-grey: #6a6a6a;
    --white: #ffffff;
    --divider: #8a8a8a;
  }
  * { margin: 0; padding: 0; box-sizing: border-box; }
  html, body {
    width: 1200px;
    height: 900px;
    overflow: hidden;
    background: var(--stage);
  }
  .stage {
    width: 1200px;
    height: 900px;
    display: flex;
    flex-direction: column;
    align-items: center;
    justify-content: center;
    gap: 40px;
  }
  .card {
    width: 620px;
    height: 378px;
    position: relative;
    box-shadow: 0 10px 30px rgba(0, 0, 0, 0.45);
  }
  .card--front {
    background: var(--card-light);
    display: flex;
    flex-direction: column;
    align-items: center;
  }
  .brand {
    margin-top: 138px;
    display: flex;
    align-items: center;
    gap: 12px;
  }
  .brand__mark {
    width: 26px;
    height: 26px;
    background: var(--brand-red);
  }
  .brand__name {
    font-family: "Poppins", sans-serif;
    font-weight: 500;
    font-size: 52px;
    line-height: 1;
    color: var(--ink-grey);
    letter-spacing: 0.5px;
  }
  .website-line {
    margin-top: 62px;
    font-family: "Roboto", sans-serif;
    font-size: 15px;
    letter-spacing: 5px;
    color: var(--url-grey);
  }
  .card--back {
    background: var(--card-dark);
    display: flex;
    align-items: center;
    justify-content: center;
  }
  .identity {
    text-align: right;
    padding-right: 24px;
  }
  .identity__name {
    font-family: "Roboto Condensed", sans-serif;
    font-weight: 700;
    font-size: 34px;
    line-height: 1;
    color: var(--brand-red);
    text-transform: uppercase;
  }
  .identity__role {
    margin-top: 6px;
    font-family: "Roboto", sans-serif;
    font-weight: 500;
    font-size: 17px;
    color: var(--white);
    text-transform: uppercase;
    letter-spacing: 0.5px;
  }
  .divider {
    width: 2px;
    height: 78px;
    background: var(--divider);
  }
  .contact-list {
    list-style: none;
    padding-left: 22px;
  }
  .contact-list__item {
    display: flex;
    align-items: center;
    gap: 10px;
    font-family: "Roboto", sans-serif;
    font-size: 17px;
    color: var(--white);
    line-height: 25px;
  }
  .contact-list__icon {
    width: 14px;
    height: 14px;
    flex: none;
  }
</style>
</head>
<body>
<main class="stage">
  <section class="card card--front" aria-label="Business card front">
    <div class="brand">
      <span class="brand__mark"></span>
      <span class="brand__name">quarvelhome</span>
    </div>
    <p class="website-line">www.quarvelhome.com.au</p>
  </section>

  <section class="card card--back" aria-label="Business card back">
    <div class="identity">
      <h1 class="identity__name">Rosalind Tebb</h1>
      <p class="identity__role">Licensee / Director</p>
    </div>
    <div class="divider"></div>
    <ul class="contact-list">
      <li class="contact-list__item">
        <svg class="contact-list__icon" viewBox="0 0 14 14" aria-hidden="true">
          <rect x="3" y="0.5" width="8" height="13" rx="1.5" fill="none" stroke="var(--brand-red)" stroke-width="1.6"/>
          <circle cx="7" cy="11" r="0.9" fill="var(--brand-red)"/>
        </svg>
        0452 918 604
      </li>
      <li class="contact-list__item">
        <svg class="contact-list__icon" viewBox="0 0 14 14" aria-hidden="true">
          <rect x="0.5" y="2.5" width="13" height="9" fill="var(--brand-red)"/>
          <path d="M0.5 2.8 L7 7.6 L13.5 2.8" fill="none" stroke="var(--card-dark)" stroke-width="1.2"/>
        </svg>
        rosalind@quarvelhome.com.au
      </li>
      <li class="contact-list__item">
        <svg class="contact-list__icon" viewBox="0 0 14 14" aria-hidden="true">
          <circle cx="7" cy="7" r="6.5" fill="var(--brand-red)"/>
          <ellipse cx="7" cy="7" rx="2.6" ry="6.3" fill="none" stroke="var(--card-dark)" stroke-width="1"/>
          <line x1="0.5" y1="7" x2="13.5" y2="7" stroke="var(--card-dark)" stroke-width="1"/>
        </svg>
        quarvelhome.com.au
      </li>
    </ul>
  </section>
</main>
</body>
</html>
```